Torvane Center for Restorative Medicine

I need a full informational website for my medical practice. I would like to use my logo and also include a lot of emblems/pictures (also a picture of me in a white coat). The website should have a function for people to inquire and send me messages. I will be offering needle-less regenerative injection therapy, stem cell treatments, bioidentical hormone therapy, treatment for chronic illness, neurodegenerative diseases, skin rejuvenation, hair restoration, male enhancement, female enhancement, and anti-aging. The practice will not be accepting insurance and will be cash/credit card only.
A good example of written content and functionality is this website:
http://thebqvx.example/. However, I want different theme and tones.
Target Market(s)
High end clientele in Los Angeles, Southern California. Health minded people who are interested in living better and longer and can afford anti-aging treatments. Men and women who want to improve sexual health and wellbeing.
Industry/Entity Type
Medical And Science
Coding
Coded - Design and coding required
Number of Pages Required
5+ page
Font styles to use
Requirements
Must have
- 1. I will need to be able to move the site to other servers (needed for site speed)
- 2. Site must be build on WordPress
- 3. Full admin credentials for domain, cpanel, wordpress, ftp.
- 4. No third party interaction on development and content deployment once the site is on different servers
- 5. I will need the ability to add content and links to the site
- 6. I will need the ability to optimize the site for speed
- 7. I will need to ability to modify URLs so they are more SEO friendly
Nice to have
- pictures of stem cells, health improvement and regeneration, beauty, youthful individuals, older healthy and happy individuals. Medical designs.
Should not have
- flowers, dna

```html
<!DOCTYPE html>
<html lang="en">
<head>
<meta charset="utf-8">
<title>Torvane Center for Restorative Medicine</title>
<link href="https://fonts.googleapis.com/css2?family=Open+Sans:wght@300;400;600&display=swap" rel="stylesheet">
<style>
:root{
  --navy:#0d2477;
  --green:#1aaa7e;
  --sky:#1a8fd0;
  --ink:#2b2b2b;
  --muted:#7a7a7a;
  --white:#ffffff;
}
*{margin:0;padding:0;box-sizing:border-box}
html,body{width:1200px;height:1146px;overflow:hidden;background:var(--white)}
body{position:relative;font-family:"Open Sans",sans-serif;color:var(--ink)}
.site-header{position:absolute;left:0;top:0;width:1200px;height:70px}
.brand{position:absolute;left:0;top:0;width:293px;height:70px;background:var(--white);display:flex;align-items:center;padding-left:131px;gap:8px}
.brand-dot{width:12px;height:12px;border-radius:50%;background:var(--navy)}
.brand-name{font-weight:600;font-size:20px;color:var(--navy);letter-spacing:.5px}
.main-nav{position:absolute;left:293px;top:0;width:907px;height:70px;background:var(--navy)}
.main-nav a{position:absolute;top:25px;font-size:13px;color:var(--white);text-decoration:none;font-weight:400}
.phone{position:absolute;left:632px;top:22px;display:flex;align-items:center;gap:12px;color:var(--white);font-weight:600;font-size:15px}
.hero{position:absolute;left:0;top:70px;width:1200px;height:454px}
.hero-photo{position:absolute;inset:0;background:linear-gradient(90deg,#f8f9fc 0%,#f6f8fc 40%,#e3e9f2 62%,#d6dde8 80%,#c9ced6 100%)}
.hero-title{position:absolute;left:131px;top:124px;font-weight:300;font-size:37px;line-height:48px;color:var(--ink)}
.hero-sub{position:absolute;left:131px;top:236px;font-weight:300;font-size:19px;color:var(--ink)}
.btn{position:absolute;left:131px;top:290px;width:107px;height:34px;background:var(--green);color:var(--white);font-size:16px;font-weight:300;display:flex;align-items:center;justify-content:center}
.doctor-photo{position:absolute;left:0;top:604px;width:565px;height:342px;background:radial-gradient(circle at 50% 45%,#e4e8ed 0%,#eef3f6 45%,#f4f9fb 100%)}
.welcome{position:absolute;left:601px;top:624px;width:470px}
.welcome-kicker{font-weight:300;font-size:19px;color:var(--sky)}
.welcome-title{margin-top:12px;font-weight:300;font-size:29px;line-height:38px;color:var(--ink)}
.welcome-text{margin-top:40px;font-weight:300;font-size:13px;line-height:25.6px;color:var(--muted);width:452px}
.services{position:absolute;left:0;top:1018px;width:1200px;text-align:center}
.services-title{font-weight:300;font-size:30px;color:var(--ink)}
.services-text{margin:12px auto 0;width:420px;font-weight:300;font-size:13px;line-height:22.4px;color:var(--muted)}
</style>
</head>
<body>
<header class="site-header">
  <div class="brand"><span class="brand-dot"></span><span class="brand-name">Torvane</span></div>
  <nav class="main-nav">
    <a style="left:38px">Home</a>
    <a style="left:105px">About</a>
    <a style="left:171px">Services</a>
    <a style="left:248px">science</a>
    <a style="left:323px">Testimonials</a>
    <a style="left:426px">Dr. Aldren Videos</a>
    <a style="left:547px">Contact</a>
    <div class="phone">
      <svg width="24" height="24" viewBox="0 0 24 24" fill="none" stroke="#fff" stroke-width="1.2"><path d="M5 3l3 0 2 5-2 1.5a11 11 0 0 0 6 6l1.5-2 5 2v3a2 2 0 0 1-2 2A17 17 0 0 1 3 5a2 2 0 0 1 2-2z"/><path d="M15 3a6 6 0 0 1 6 6M15 6a3 3 0 0 1 3 3"/></svg>
      <span>+1 818 555 0142</span>
    </div>
  </nav>
</header>

<section class="hero">
  <div class="hero-photo" role="img" aria-label="Bright clinical treatment room with overhead examination light"></div>
  <h1 class="hero-title">Regenerative medicine is the<br>medicine of the future.</h1>
  <p class="hero-sub">It is time that we go back to the origin</p>
  <a class="btn">Read More</a>
</section>

<div class="doctor-photo" role="img" aria-label="Portrait of the physician in a white coat with stethoscope, arms crossed"></div>
<section class="welcome">
  <p class="welcome-kicker">Welcome to</p>
  <h2 class="welcome-title">Torvane Center for Restorative Medicine</h2>
  <p class="welcome-text">Lorem ipsum dolor sit amet, consectetur adipiscing elit, sed do eiusmod tempor incididunt ut labore et dolore magna aliqua. Ut enim ad minim veniam, quis nostrud exercitation ullamco laboris nisi ut aliquip ex ea commodo consequat. Duis aute irure dolor in reprehenderit in voluptate velit esse cillum dolore eu fugiat nulla pariatur. Excepteur sint occaecat cupidatat non proident, sunt in culpa qui officia deserunt mollit anim id est laborum.</p>
</section>

<section class="services">
  <h2 class="services-title">OUR SERVICES</h2>
  <p class="services-text">Lorem ipsum dolor sit amet, consectetur adipiscing elit, sed do eiusmod tempor incididunt ut labore et dolore magna aliqua.</p>
</section>
</body>
</html>
```